Patient Transport company website design

We're a small patient transport company desiring a big company image. Our company is called Plovatrin. We're based in Houston, TX. Our mission is to provide a safe, cost effective, and convenient mode of local transportation. Similar to a taxi service but more patient friendly.
We would like to see designs that illustrate our mission and have a big company online presence. We like bright colors but not too bright and cartoon-like. Our target audience are patients but we also cater to elderly as well as those who might not have reliable transportation.
We're not an emergency transport service. We're not a taxi service. We're more like a shuttle service... a compromise between the two. Photography for the site should show patients and elderly riding in normal (unmarked vehicles) to and from dr visits, etc.
Our competitors' websites are listed here to give you a general idea about the industry.
http://www.kelbrookmedicalrides.example/
http://www.trundlevan.example/
http://www.ferroquinpatientrides.example/
Target Market(s)
Patients needing transportation assistance and Elderly as well.
Industry/Entity Type
Taxi
Requirements
Must have
- Website must be done in wordpress. Website must have the following links:
Services, About, Book a trip, jobs, control panel, clients
Should use photos communicating safe travels to and from... particularly with Elderly if possible.
Design should be consistent with attached logo.
Nice to have
- Bright colors

```html
<!DOCTYPE html>
<html lang="en">
<head>
<meta charset="utf-8">
<title>Plovatrin — Patient Transportation Services</title>
<link rel="stylesheet" href="https://fonts.googleapis.com/css2?family=Open+Sans:wght@400;600;700&display=swap">
<style>
  :root {
    --teal: #0aa6c8;
    --teal-dark: #1b8595;
    --navy: #0d4a8b;
    --lime: #9dc43c;
    --lime-text: #a3c93a;
    --sky: #a7dff0;
    --charcoal: #222528;
    --field: #3a3d42;
    --paper: #ffffff;
    --mist: #f5f5f5;
    --ink: #2b2b2b;
    --grey-text: #8a8a8a;
    --link-blue: #3d6fa7;
    --red: #b10d0d;
  }
  * { box-sizing: border-box; margin: 0; padding: 0; }
  html, body { width: 1200px; height: 1136px; overflow: hidden; }
  body { position: relative; background: var(--paper); font-family: "Open Sans", Arial, sans-serif; color: var(--ink); }
  .abs { position: absolute; }

  /* Header */
  .brand { left: 182px; top: 28px; display: flex; align-items: center; gap: 10px; }
  .brand-dot { width: 34px; height: 34px; border-radius: 50%; background: var(--lime); }
  .brand-name { font-size: 34px; font-weight: 600; color: var(--navy); line-height: 1; }
  .brand-tag { left: 174px; top: 98px; font-size: 10px; font-weight: 700; color: var(--navy); }
  .search { left: 609px; top: 31px; display: flex; }
  .search-field { width: 211px; height: 31px; border: 1px solid #c9dd9a; border-right: 0; background: var(--mist); font-size: 11px; color: #777; padding: 8px 10px; }
  .search-btn { width: 98px; height: 31px; background: var(--lime); color: #fff; font-size: 13px; font-weight: 600; text-align: center; line-height: 31px; }
  .social { width: 32px; height: 32px; border-radius: 50%; }
  .social.a { background: #3b5c9e; }
  .social.b { background: #29a6e0; }
  .top-links { right: 173px; top: 90px; font-size: 13px; letter-spacing: .3px; color: var(--teal); }
  .top-links span { margin: 0 6px; }
  .top-links .home { color: var(--link-blue); }
  .top-links .contact { color: #8db432; font-weight: 600; }

  /* Nav */
  .nav { left: 0; top: 125px; width: 1200px; height: 36px; background: var(--teal); }
  .nav-item { top: 6px; font-size: 17px; color: #fff; white-space: nowrap; }
  .nav-sep { top: 8px; width: 1px; height: 20px; background: rgba(255,255,255,.35); }

  /* Hero */
  .hero-band { left: 0; top: 161px; width: 1200px; height: 358px; background: var(--mist); }
  .hero-frame { left: 166px; top: 162px; width: 866px; height: 358px; background: var(--teal); box-shadow: 0 3px 6px rgba(0,0,0,.3); }
  .hero-photo { left: 174px; top: 170px; width: 851px; height: 312px; background: linear-gradient(100deg, #2d3a2f 0%, #a7853f 30%, #c9a560 50%, #b8b3a8 70%, #4a3a6a 100%); }
  .hero-caption { left: 166px; top: 482px; width: 866px; height: 38px; background: #0b0b0b; color: var(--lime-text); font-size: 19px; font-weight: 600; letter-spacing: 1px; text-align: center; line-height: 38px; }
  .hero-arrow { top: 309px; width: 28px; height: 53px; background: var(--teal-dark); color: #fff; font-size: 20px; font-weight: 700; text-align: center; line-height: 53px; }

  /* Dropdown */
  .dropdown { left: 302px; top: 165px; width: 188px; height: 98px; background: var(--teal); }
  .drop-item { left: 0; width: 188px; height: 29px; font-size: 11.5px; font-weight: 600; letter-spacing: -0.2px; color: #fff; padding: 0 12px; line-height: 29px; white-space: nowrap; }
  .drop-item.active { background: var(--lime); color: #1e2a10; }
  .drop-rule { left: 42px; width: 134px; border-top: 1px dashed rgba(255,255,255,.8); }

  /* Services */
  .services { left: 0; top: 519px; width: 1200px; height: 371px; background: var(--sky); }
  .card { top: 542px; width: 247px; height: 314px; background: var(--paper); box-shadow: 0 3px 5px rgba(0,0,0,.35); }
  .card-head { left: 0; top: 0; width: 247px; height: 100px; background: var(--navy); }
  .card-title { left: 0; top: 9px; width: 247px; text-align: center; color: #fff; font-size: 17px; line-height: 22px; }
  .card-photo { left: 21px; top: 54px; width: 205px; height: 125px; border-bottom: 3px solid var(--navy); }
  .card-icons { left: 0; top: 190px; width: 247px; display: flex; justify-content: center; gap: 11px; }
  .card-icons .social { width: 30px; height: 30px; }
  .card-text { left: 20px; top: 232px; width: 210px; font-size: 11px; line-height: 14.5px; color: var(--grey-text); }
  .card-more { left: 0; top: 292px; width: 247px; text-align: center; font-size: 10.5px; font-weight: 700; color: var(--red); }

  /* Lower */
  .lower { left: 0; top: 890px; width: 1200px; height: 187px; background: var(--charcoal); }
  .tab { top: 866px; width: 252px; height: 56px; }
  .tab-title { left: 24px; top: 30px; color: #fff; font-size: 17px; white-space: nowrap; }
  .list { width: 200px; list-style: none; font-size: 11px; line-height: 14px; color: #fff; }
  .list li { position: relative; padding-left: 22px; margin-bottom: 12px; }
  .list li::before { content: ""; position: absolute; left: 0; top: 7px; width: 8px; height: 8px; border-radius: 50%; background: var(--lime); }
  .field { left: 779px; width: 214px; height: 30px; background: var(--field); font-size: 11px; color: #a5a8ad; padding: 7px 10px; }
  .submit { left: 918px; top: 1025px; width: 75px; height: 29px; background: var(--lime); color: #111; font-size: 13px; text-align: center; line-height: 29px; }

  /* Footer */
  .foot-links { left: 0; top: 1077px; width: 1200px; height: 31px; background: var(--navy); color: #fff; font-size: 11.5px; text-align: center; line-height: 31px; white-space: nowrap; }
  .foot-copy { left: 0; top: 1108px; width: 1200px; height: 28px; background: var(--lime); color: #1a1a1a; font-size: 11.5px; text-align: center; line-height: 28px; }
</style>
</head>
<body>

<header>
  <div class="abs brand"><span class="brand-dot"></span><span class="brand-name">Plovatrin</span></div>
  <div class="abs brand-tag">Patient Transportation Services</div>
  <div class="abs search"><div class="search-field">Type Here . . .</div><div class="search-btn">SEARCH</div></div>
  <div class="abs social a" style="left:950px;top:32px"></div>
  <div class="abs social b" style="left:993px;top:32px"></div>
  <div class="abs top-links"><span class="home">HOME</span>|<span class="contact">CONTACT US</span>|<span>STAFF&nbsp; LOGIN</span></div>
</header>

<nav class="abs nav">
  <div class="abs nav-item" style="left:193px">About Us</div>
  <div class="abs nav-sep" style="left:302px"></div>
  <div class="abs nav-item" style="left:308px">What we do</div>
  <div class="abs nav-sep" style="left:439px"></div>
  <div class="abs nav-item" style="left:449px">Service Area</div>
  <div class="abs nav-sep" style="left:584px"></div>
  <div class="abs nav-item" style="left:602px">Payment Options</div>
  <div class="abs nav-item" style="left:790px">Careers</div>
  <div class="abs nav-item" style="left:900px">Appointments</div>
</nav>

<section>
  <div class="abs hero-band"></div>
  <div class="abs hero-frame"></div>
  <div class="abs hero-photo" role="img" aria-label="Photo of two care staff smiling with an elderly patient in a hospital gown"></div>
  <div class="abs hero-arrow" style="left:174px">&#10094;</div>
  <div class="abs hero-arrow" style="left:997px">&#10095;</div>
  <div class="abs hero-caption">PATIENT &nbsp;TRANSPORTAION &nbsp;SERVICES</div>
</section>

<div class="abs dropdown">
  <div class="abs drop-item active" style="top:0">Door to Door Transportation</div>
  <div class="abs drop-item" style="top:33px">Medical Appointments</div>
  <div class="abs drop-rule" style="top:64px"></div>
  <div class="abs drop-item" style="top:66px">Social Appointments</div>
</div>

<section class="abs services"></section>

<article class="abs card" style="left:193px">
  <div class="abs card-head"></div>
  <div class="abs card-title">DOOR TO DOOR<br>TRANSPORTATION</div>
  <div class="abs card-photo" role="img" aria-label="Photo of a carer helping a senior in a wheelchair beside a van" style="background:linear-gradient(90deg,#8a8c8e,#c9c7c3 55%,#e8e6e2)"></div>
  <div class="abs card-icons"><span class="social a"></span><span class="social b"></span></div>
  <p class="abs card-text">Lorem Ipsum Dolor sit ame, cons adipisi elit dower hen. &nbsp; Lorem Ipsum Dolor sit ame, cons adipisi elit dower hen.</p>
  <div class="abs card-more">READ MORE</div>
</article>

<article class="abs card" style="left:479px">
  <div class="abs card-head"></div>
  <div class="abs card-title" style="top:12px">MEDICAL APPOINTMENT</div>
  <div class="abs card-photo" role="img" aria-label="Photo of a doctor talking with an elderly patient" style="background:linear-gradient(90deg,#d9d6d2,#b7b4b0 50%,#e3e7ea)"></div>
  <div class="abs card-icons"><span class="social a"></span><span class="social b"></span></div>
  <p class="abs card-text">Lorem Ipsum Dolor sit ame, cons adipisi elit dower hen. &nbsp; Lorem Ipsum Dolor sit ame, cons adipisi elit dower hen.</p>
  <div class="abs card-more">READ MORE</div>
</article>

<article class="abs card" style="left:760px">
  <div class="abs card-head"></div>
  <div class="abs card-title" style="top:12px">SOCIAL APPOINTMENTS</div>
  <div class="abs card-photo" role="img" aria-label="Photo of a smiling senior woman looking out of a car window" style="background:linear-gradient(180deg,#6f7b8c,#a9b3c0 60%,#e6eaf0)"></div>
  <div class="abs card-icons"><span class="social a"></span><span class="social b"></span></div>
  <p class="abs card-text">Lorem Ipsum Dolor sit ame, cons adipisi elit dower hen. &nbsp; Lorem Ipsum Dolor sit ame, cons adipisi elit dower hen.</p>
  <div class="abs card-more">READ MORE</div>
</article>

<section class="abs lower"></section>

<svg class="abs tab" style="left:191px" viewBox="0 0 252 56" aria-hidden="true">
  <rect x="0" y="24" width="252" height="32" fill="#1d7f8e"/>
  <polygon points="212,24 226,24 234,56 220,56" fill="#2aa7b7"/>
  <polygon points="224,0 232,0 252,56 240,56" fill="#0aa6c8"/>
</svg>
<div class="abs tab-title" style="left:215px;top:896px">CASE HISTORIES</div>

<svg class="abs tab" style="left:478px" viewBox="0 0 252 56" aria-hidden="true">
  <rect x="0" y="24" width="252" height="32" fill="#1d7f8e"/>
  <polygon points="212,24 226,24 234,56 220,56" fill="#2aa7b7"/>
  <polygon points="224,0 232,0 252,56 240,56" fill="#0aa6c8"/>
</svg>
<div class="abs tab-title" style="left:502px;top:896px">LATEST NEWS</div>

<svg class="abs tab" style="left:760px" viewBox="0 0 252 56" aria-hidden="true">
  <rect x="0" y="24" width="252" height="32" fill="#1d7f8e"/>
  <polygon points="212,24 226,24 234,56 220,56" fill="#2aa7b7"/>
  <polygon points="224,0 232,0 252,56 240,56" fill="#0aa6c8"/>
</svg>
<div class="abs tab-title" style="left:782px;top:896px">SUBSCRIBE NEWSLETTER</div>

<ul class="abs list" style="left:212px;top:937px">
  <li>Lorem Ipsum Dolor sit ame, cons adipisi elit dower hen.</li>
  <li>Lorem Ipsum Dolor sit ame, cons adipisi elit dower hen.</li>
  <li>Lorem Ipsum Dolor sit ame, cons adipisi elit dower hen.</li>
</ul>
<ul class="abs list" style="left:498px;top:937px">
  <li>Lorem Ipsum Dolor sit ame, cons adipisi elit dower hen.</li>
  <li>Lorem Ipsum Dolor sit ame, cons adipisi elit dower hen.</li>
  <li>Lorem Ipsum Dolor sit ame, cons adipisi elit dower hen.</li>
</ul>

<div class="abs field" style="top:943px">Name</div>
<div class="abs field" style="top:983px">Email Id</div>
<div class="abs submit">SUBMIT</div>

<footer>
  <div class="abs foot-links">Home | About Us | What we do | Service Area | Payment Options | Careers | Appointments | &nbsp;Contact Us &nbsp;| &nbsp;Sitemap &nbsp;| &nbsp;Privacy &amp; Accessibility</div>
  <div class="abs foot-copy">© 2013 &nbsp;Plovatrin &nbsp;(Patient Transportation Services)</div>
</footer>

</body>
</html>
```